Business Card Design

I already have a company logo for my company. I have a logo for the manufacturer we represent. I want a professional business card design.

```html
<!DOCTYPE html>
<html lang="en">
<head>
<meta charset="utf-8">
<title>Beacon Hazard Group – Business Card</title>
<link href="https://fonts.googleapis.com/css2?family=Poppins:wght@400;600;700&display=swap" rel="stylesheet">
<style>
  :root {
    --backdrop: #ababab;
    --card-white: #ffffff;
    --card-black: #000000;
    --brand-red: #e31b23;
    --text-dark: #1a1a1a;
    --text-grey: #3a3a3a;
    --brand-yellow: #e2b318;
  }
  * { box-sizing: border-box; margin: 0; padding: 0; }
  html, body {
    width: 1093px; height: 1200px; overflow: hidden;
    background: var(--backdrop);
    font-family: "Poppins", sans-serif;
  }
  .canvas { position: relative; width: 1093px; height: 1200px; }

  .card {
    position: absolute; left: 264px;
    border-radius: 24px;
    overflow: hidden;
  }
  .card--front {
    top: 226px; width: 578px; height: 356px;
    background: var(--card-white);
  }
  .card--back {
    top: 621px; width: 584px; height: 360px;
    background: var(--card-black);
  }

  .person { position: absolute; left: 40px; top: 48px; }
  .person__name {
    font-weight: 700; font-size: 23px; line-height: 1;
    color: var(--brand-red); letter-spacing: 0.2px;
  }
  .person__role {
    font-weight: 400; font-size: 17.5px; line-height: 1.2;
    color: var(--text-grey); margin-top: 2px;
  }

  .contact-list { position: absolute; left: 40px; top: 145px; list-style: none; }
  .contact-list li {
    display: flex; align-items: center; gap: 7px;
    font-size: 17.5px; line-height: 21px; color: var(--text-dark);
  }
  .contact-list svg { width: 15px; height: 15px; flex: none; }
  .contact-list .accent { color: var(--brand-red); }

  .address {
    position: absolute; left: 40px; top: 268px;
    font-size: 17.5px; line-height: 21px; color: var(--text-dark);
  }

  .brand-front {
    position: absolute; left: 300px; top: 0; width: 278px; height: 356px;
    display: flex; flex-direction: column; align-items: center; justify-content: center; gap: 14px;
  }
  .brand-front__mark {
    width: 74px; height: 74px; border-radius: 50%;
    background: var(--brand-yellow);
  }
  .brand-front__name {
    font-weight: 700; font-size: 26px; line-height: 1.1;
    color: var(--brand-red); text-align: center; text-transform: uppercase;
  }

  .brand-back {
    position: absolute; inset: 0;
    display: flex; flex-direction: column; align-items: center; justify-content: center; gap: 16px;
  }
  .brand-back__mark {
    width: 60px; height: 60px;
    background: var(--brand-yellow);
  }
  .brand-back__name {
    font-weight: 700; font-size: 30px; line-height: 1.1;
    color: var(--brand-red); text-align: center; text-transform: uppercase;
  }
</style>
</head>
<body>
<main class="canvas">

  <section class="card card--front" aria-label="Business card front">
    <div class="person">
      <h1 class="person__name">DANIEL MARSH</h1>
      <p class="person__role">Managing Director</p>
    </div>

    <ul class="contact-list">
      <li>
        <svg viewBox="0 0 24 24" aria-hidden="true"><path fill="#e31b23" d="M6.6 10.8a15.1 15.1 0 0 0 6.6 6.6l2.2-2.2c.3-.3.7-.4 1-.2 1.1.4 2.3.6 3.6.6.6 0 1 .4 1 1V20c0 .6-.4 1-1 1A17 17 0 0 1 3 4c0-.6.4-1 1-1h3.5c.6 0 1 .4 1 1 0 1.3.2 2.5.6 3.6.1.3 0 .7-.2 1z"/></svg>
        044-555 218 630
      </li>
      <li>
        <svg viewBox="0 0 24 24" aria-hidden="true"><rect x="2" y="5" width="20" height="14" fill="#e31b23"/><path d="M2 5l10 8 10-8" stroke="#fff" stroke-width="1.6" fill="none"/></svg>
        hello@beaconhazard.com
      </li>
      <li>
        <svg viewBox="0 0 24 24" aria-hidden="true"><g fill="none" stroke="#e31b23" stroke-width="2"><circle cx="12" cy="12" r="9.5"/><ellipse cx="12" cy="12" rx="4.2" ry="9.5"/><path d="M2.5 12h19M4 7h16M4 17h16"/></g></svg>
        <span>www.<span class="accent">beaconhazard</span>.com</span>
      </li>
    </ul>

    <p class="address">87, Harbor Works Road<br>45460, Eastland</p>

    <div class="brand-front">
      <span class="brand-front__mark" aria-hidden="true"></span>
      <span class="brand-front__name">Beacon Hazard<br>Group LLC</span>
    </div>
  </section>

  <section class="card card--back" aria-label="Business card back">
    <div class="brand-back">
      <span class="brand-back__mark" aria-hidden="true"></span>
      <span class="brand-back__name">Beacon Hazard<br>Group LLC</span>
    </div>
  </section>

</main>
</body>
</html>
```